Kestrel Roofing & Restoration Business Card Design

Lookiing for a double sided business card design that will have rounded corners, will look good with Spot UV, Soft Laminate, or Gloss
Front of card should have Logo, Name and Contact Info, License numbers
Back of card should have Logo, maybe other small details

```html
<!DOCTYPE html>
<html lang="en">
<head>
<meta charset="utf-8">
<title>Kestrel Roofing &amp; Restoration — Business Card</title>
<link href="https://fonts.googleapis.com/css2?family=Montserrat:wght@400;500;700&display=swap" rel="stylesheet">
<style>
  :root {
    --ink: #1e1d1f;
    --sky: #1aa7e0;
    --paper: #ffffff;
    --stage: #ece8e1;
    --text: #1e1d1f;
    --faint: #eeeff1;
  }
  html, body {
    margin: 0;
    width: 1200px;
    height: 900px;
    overflow: hidden;
    background: var(--stage);
    font-family: "Montserrat", Arial, sans-serif;
  }
  .sheet {
    position: relative;
    width: 1200px;
    height: 900px;
  }
  .card {
    position: absolute;
    width: 560px;
    height: 320px;
    border-radius: 14px;
    overflow: hidden;
    box-shadow: 0 10px 28px rgba(0,0,0,0.14);
  }
  .card svg { display: block; width: 100%; height: 100%; }
  .card--front { left: 320px; top: 100px; background: var(--paper); }
  .card--back { left: 320px; top: 480px; background: var(--ink); }

  .brand-name { font-family: "Montserrat", Arial, sans-serif; font-weight: 700; fill: #ffffff; letter-spacing: 1px; }
  .brand-ghost { font-family: "Montserrat", Arial, sans-serif; font-weight: 700; fill: var(--faint); }
  .person-name { font-family: "Montserrat", Arial, sans-serif; font-weight: 700; font-size: 24px; fill: #ffffff; letter-spacing: 1px; }
  .person-role { font-family: "Montserrat", Arial, sans-serif; font-weight: 400; font-size: 11px; fill: #ffffff; letter-spacing: 0.5px; }
  .contact { font-family: "Montserrat", Arial, sans-serif; font-weight: 500; font-size: 14.5px; fill: var(--text); }
  .contact-label { fill: var(--sky); }
</style>
</head>
<body>
<main class="sheet">

  <section class="card card--front" aria-label="Business card front">
    <svg viewBox="0 0 560 320" xmlns="http://www.w3.org/2000/svg">
      <text class="brand-ghost" x="250" y="282" font-size="54">KESTREL</text>

      <polygon class="roof-dark" fill="var(--ink)" points="240,0 560,0 560,250"/>
      <polygon class="roof-stripe" fill="var(--sky)" points="105,72 240,0 560,250 560,295 240,45 160,72"/>
      <polygon class="name-bar" fill="var(--ink)" points="0,85 291,85 349,130 0,130"/>

      <text class="person-name" x="38" y="112">JOHN SMITH</text>
      <text class="person-role" x="38" y="125">Designation</text>

      <g class="contact-list">
        <text class="contact" x="70" y="170"><tspan class="contact-label">L NO :</tspan> EL123456</text>

        <g class="icon icon--phone" transform="translate(30,184)">
          <rect width="17" height="15" rx="3" fill="var(--sky)"/>
          <path d="M5 4 q-1 4 4 7 l2 -1.5 -2-2 -1 1 q-2-1-2-3 l1-1 -2-2z" fill="#fff"/>
        </g>
        <text class="contact" x="64" y="197">(123) 444-5555</text>

        <g class="icon icon--mail" transform="translate(30,208)">
          <rect width="17" height="15" rx="3" fill="var(--sky)"/>
          <rect x="3.5" y="4" width="10" height="7" fill="none" stroke="#fff" stroke-width="1.2"/>
          <path d="M3.5 4 l5 4 5-4" fill="none" stroke="#fff" stroke-width="1.2"/>
        </g>
        <text class="contact" x="64" y="221">your@email.com</text>

        <g class="icon icon--web" transform="translate(30,232)">
          <rect width="17" height="15" rx="3" fill="var(--sky)"/>
          <circle cx="8.5" cy="7.5" r="4.8" fill="none" stroke="#fff" stroke-width="1.1"/>
          <ellipse cx="8.5" cy="7.5" rx="2" ry="4.8" fill="none" stroke="#fff" stroke-width="1"/>
          <line x1="3.7" y1="7.5" x2="13.3" y2="7.5" stroke="#fff" stroke-width="1"/>
        </g>
        <text class="contact" x="64" y="245">www.yourwebsite.com</text>
      </g>

      <g class="brand-lockup" transform="translate(372,28) rotate(38)">
        <rect x="0" y="-15" width="15" height="15" fill="var(--sky)"/>
        <text class="brand-name" x="22" y="0" font-size="19">KESTREL</text>
        <text class="brand-name" x="22" y="19" font-size="12">ROOFING &amp;</text>
        <text class="brand-name" x="22" y="34" font-size="12">RESTORATION</text>
      </g>
    </svg>
  </section>

  <section class="card card--back" aria-label="Business card back">
    <svg viewBox="0 0 560 320" xmlns="http://www.w3.org/2000/svg">
      <g class="brand-lockup">
        <rect x="104" y="135" width="28" height="28" fill="var(--sky)"/>
        <text class="brand-name" x="146" y="162" font-size="36">KESTREL</text>
        <line x1="346" y1="128" x2="346" y2="192" stroke="#ffffff" stroke-width="1.2"/>
        <text class="brand-name" x="360" y="152" font-size="17">ROOFING &amp;</text>
        <text class="brand-name" x="360" y="178" font-size="17">RESTORATION</text>
      </g>
    </svg>
  </section>

</main>
</body>
</html>
```